Custom Manufacturing Job Shop

We are looking for a business card design for Tall Oak Fabrication Inc. Tall Oak is a family owned business that manufactures any custom product to fit a customers needs, whether it is custom 1 piece or production parts, we truly take on projects that others just cant do. to help in your design go to www.talloakfab.example for a more in depth idea. we have the following capabilities that we would like to see on the card somewhere...maybe on the back of a 2 sided card? we are fully open to ideas.
Machining
• Fabrication
• Millwork
• Maintenance
• Laser Cutting
• Precision Forming
Engineering
Blasting/Painting

No matter how big or small, We literally do it all

preferably black or darker cards but we don't mind to see some color if you see a better fit. we are interested in looking at anything that catches attention.
I have attached our logo, if it is needed in a different file type please let me know and I will send it to you if I can. maybe adding some type of drawing or dimensional lines would be something to add?? just throwing ideas out there....

Reason: I added one of our shredder designs and would like to see a few more cards if possible using this. any questions please don't hesitate to ask!!

Target Market(s)

anyone looking for design/manufacturing/machining whether it is custom 1 off parts or production.

Industry/Entity Type

Business

Contact Information for Business Card

preferably darker shades, but also not opposed to some color in the same sense....not too bright

Font styles to use
Serif
Sans Serif

Requirements
Must have
• Dell Marwick
• Direct:555-213-7790
• Cell:555-348-1162
• Fax: 555-907-4425
• 42 Quarry Lane
• Klingerstown, PA 00000
• I also would request having it in a format I can give to the company making the business cards to edit names/numbers etc. for the entire staff.
Nice to have
• drafting lines? we are open to almost anything....
Should not have
• exotic colors

```html
<!DOCTYPE html>
<html lang="en">
<head>
<meta charset="utf-8">
<title>Tall Oak Fabrication Inc. — Business Card</title>
<link rel="stylesheet" href="https://fonts.googleapis.com/css2?family=Open+Sans:wght@400;600;700&display=swap">
<style>
  :root {
    --backdrop: #d8d5d1;
    --card-deep: #0b0b0c;
    --card-mid: #1c1d1f;
    --card-sheen: #2e3033;
    --tab-white: #e9e9ea;
    --text-white: #f2f2f2;
    --accent-blue: #2f86c8;
    --mark-grey: #d9dadb;
  }
  * { box-sizing: border-box; margin: 0; padding: 0; }
  html, body {
    width: 1200px;
    height: 418px;
    overflow: hidden;
    background: var(--backdrop);
    font-family: "Open Sans", Arial, sans-serif;
  }
  .stage { position: relative; width: 1200px; height: 418px; }

  .card {
    position: absolute;
    top: 65px;
    width: 464px;
    height: 264px;
    border-radius: 21px;
    overflow: hidden;
    background:
      repeating-linear-gradient(90deg, rgba(255,255,255,0.018) 0 1px, rgba(0,0,0,0) 1px 3px),
      linear-gradient(90deg, var(--card-deep) 0%, var(--card-sheen) 22%, var(--card-deep) 40%, var(--card-mid) 62%, var(--card-sheen) 78%, var(--card-deep) 100%);
    box-shadow: 0 3px 8px rgba(0,0,0,0.35);
  }
  .card::after {
    content: "";
    position: absolute;
    inset: 0;
    background: linear-gradient(180deg, rgba(255,255,255,0.05) 0%, rgba(0,0,0,0) 45%, rgba(0,0,0,0.35) 100%);
    pointer-events: none;
  }
  .card--front { left: 101px; }
  .card--back { left: 616px; }

  .edge-tab {
    position: absolute;
    top: 81px;
    width: 12px;
    height: 105px;
    background: var(--tab-white);
  }
  .edge-tab--left { left: 0; }
  .edge-tab--right { right: 0; }

  .brand {
    position: absolute;
    display: flex;
    align-items: center;
    gap: 10px;
    z-index: 1;
  }
  .brand__dot {
    width: 16px;
    height: 16px;
    border-radius: 50%;
    background: var(--mark-grey);
  }
  .brand__name {
    font-weight: 700;
    font-size: 40px;
    line-height: 1;
    color: var(--mark-grey);
    letter-spacing: 0.5px;
  }
  .card--front .brand { left: 42px; top: 38px; }
  .card--back .brand { left: 200px; top: 98px; }

  .holder-name {
    position: absolute;
    left: 41px;
    top: 208px;
    font-size: 18px;
    font-weight: 600;
    color: var(--accent-blue);
    letter-spacing: 0.6px;
    z-index: 1;
  }

  .contact {
    position: absolute;
    right: 40px;
    top: 159px;
    text-align: right;
    list-style: none;
    font-size: 12px;
    line-height: 19.5px;
    color: var(--text-white);
    z-index: 1;
  }
  .contact__label { color: var(--accent-blue); font-weight: 600; }
  .contact__address { color: var(--accent-blue); }

  .services-title {
    position: absolute;
    left: 34px;
    top: 52px;
    font-size: 20px;
    font-weight: 600;
    color: var(--text-white);
    z-index: 1;
  }
  .services {
    position: absolute;
    left: 34px;
    top: 96px;
    list-style: none;
    font-size: 12px;
    line-height: 20.4px;
    color: var(--accent-blue);
    z-index: 1;
  }
  .services li::before { content: "• "; }
  .services-extra {
    position: absolute;
    left: 34px;
    top: 200px;
    font-size: 12px;
    color: var(--text-white);
    z-index: 1;
  }
</style>
</head>
<body>
<main class="stage">

  <section class="card card--front" aria-label="Business card front">
    <span class="edge-tab edge-tab--left"></span>
    <span class="edge-tab edge-tab--right"></span>

    <div class="brand">
      <span class="brand__dot"></span>
      <span class="brand__name">Tall Oak</span>
    </div>

    <p class="holder-name">Dell Marwick</p>

    <ul class="contact">
      <li><span class="contact__label">Direct :</span> 555-213-7790</li>
      <li><span class="contact__label">Cell :</span> 555-348-1162</li>
      <li><span class="contact__label">Fax :</span> 555-907-4425</li>
      <li class="contact__address">42 Quarry Lane</li>
    </ul>
  </section>

  <section class="card card--back" aria-label="Business card back">
    <h2 class="services-title">Machining</h2>
    <ul class="services">
      <li>Fabrication</li>
      <li>Millwork</li>
      <li>Maintenance</li>
      <li>Laser Cutting</li>
      <li>Precision Forming</li>
    </ul>
    <p class="services-extra">Engineering Blasting/Painting</p>

    <div class="brand">
      <span class="brand__dot"></span>
      <span class="brand__name">Tall Oak</span>
    </div>
  </section>

</main>
</body>
</html>
```